Halvern Properties Business Cards

I would like a business card that includes myself and my partner.
Includes: Logo, office #, email, website, our names, our numbers and possibly the address. I would also like the logo to be embossed and the card to be horizontal.
There is a photo of our yard signs to give you an idea of the colors of our business.

Target Market(s)

Everyone in real estate market.
We are in a rural area. Our clientele are from all socioeconomic backgrounds.

Industry/Entity Type

Real Estate Agent

Contact Information for Business Card

Company Name: Halvern Properties
Our Names, Titles & Cell #'s : Marla Halvern-Broker (555).316.4827, Tessa Halvern-Realtor (555).627.9154
Office #: (555).841.2600
Website: halvernproperties-example.com
Joint Email: halvern@halvernproperties-example.com
Office Address: 518B W. Cottonwell Ave.
Larkston, ST. 70999

Font styles to use
Serif

Requirements
Must have
• HORIZONTAL, Logo, Myself and my partners names, Our cell #'s, our office #, our website, our email address
Nice to have
• Embossed logo, office address, our titles.

```html
<!DOCTYPE html>
<html lang="en">
<head>
<meta charset="utf-8">
<title>Halvern Properties Business Cards</title>
<link rel="stylesheet" href="https://fonts.googleapis.com/css2?family=EB+Garamond:wght@600&family=Open+Sans:wght@400;600&display=swap">
<style>
  :root {
    --plum: #4a2267;
    --plum-card: #4b2468;
    --paper: #ffffff;
    --ink: #3b3a36;
    --backdrop: #ecebee;
    --rule: #6b5a7a;
  }
  * { box-sizing: border-box; margin: 0; padding: 0; }
  html, body { width: 1200px; height: 900px; overflow: hidden; }
  body {
    background: var(--backdrop);
    position: relative;
    font-family: "Open Sans", Arial, sans-serif;
  }
  .card {
    position: absolute;
    box-shadow: 0 6px 18px rgba(0,0,0,0.18);
  }
  .card--front {
    left: 78px; top: 35px; width: 587px; height: 363px;
    background: var(--paper);
  }
  .card--back {
    left: 388px; top: 505px; width: 567px; height: 352px;
    background: var(--plum-card);
  }

  .brand {
    position: absolute;
    display: flex;
    align-items: center;
    gap: 14px;
  }
  .brand__dot {
    width: 70px; height: 70px; border-radius: 50%;
    flex: none;
  }
  .brand__name {
    font-family: "EB Garamond", Georgia, serif;
    font-weight: 600;
    text-align: center;
    line-height: 1;
  }
  .brand__word { display: block; font-size: 54px; letter-spacing: 1px; }
  .brand__rule { display: block; height: 2px; margin: 4px 0 8px; }
  .brand__sub { display: block; font-size: 33px; }

  .card--front .brand { left: 100px; top: 52px; color: var(--plum); }
  .card--front .brand__dot { background: var(--plum); }
  .card--front .brand__rule { background: var(--plum); }

  .card--back .brand { left: 95px; top: 120px; color: var(--paper); }
  .card--back .brand__dot { background: var(--paper); }
  .card--back .brand__rule { background: var(--paper); }

  .agents {
    position: absolute; left: 0; right: 0; top: 185px;
    display: flex; justify-content: center;
  }
  .agent { padding: 0 14px; }
  .agent--left { text-align: right; border-right: 1.5px solid var(--rule); }
  .agent--right { text-align: left; }
  .agent__name {
    font-size: 19px; font-weight: 600; color: var(--plum);
    letter-spacing: 0.2px; line-height: 1.3;
  }
  .agent__role, .agent__phone {
    font-size: 15px; color: var(--ink); line-height: 1.45;
  }

  .contact {
    position: absolute; left: 0; right: 0; top: 268px;
    text-align: center; font-size: 15px; color: var(--ink);
  }
  .contact__label { font-weight: 600; color: var(--plum); }
  .address {
    position: absolute; left: 0; right: 0; top: 305px;
    text-align: center; font-size: 15px; color: var(--ink);
  }

  .website {
    position: absolute; left: 0; right: 0; top: 256px;
    text-align: center; font-size: 15px; color: var(--paper);
  }
</style>
</head>
<body>
  <section class="card card--front" aria-label="Business card front">
    <div class="brand">
      <span class="brand__dot"></span>
      <span class="brand__name">
        <span class="brand__word">HALVERN</span>
        <span class="brand__rule"></span>
        <span class="brand__sub">Properties</span>
      </span>
    </div>

    <div class="agents">
      <div class="agent agent--left">
        <p class="agent__name">MARLA HALVERN</p>
        <p class="agent__role">Broker</p>
        <p class="agent__phone">(555).316.4827</p>
      </div>
      <div class="agent agent--right">
        <p class="agent__name">TESSA HALVERN</p>
        <p class="agent__role">Realtor</p>
        <p class="agent__phone">(555).627.9154</p>
      </div>
    </div>

    <p class="contact">
      <span class="contact__label">P:</span> (555).841.2600 |
      <span class="contact__label">E:</span> halvern@halvernproperties-example.com
    </p>
    <p class="address">518B W. Cottonwell Ave. Larkston, ST. 70999</p>
  </section>

  <section class="card card--back" aria-label="Business card back">
    <div class="brand">
      <span class="brand__dot"></span>
      <span class="brand__name">
        <span class="brand__word">HALVERN</span>
        <span class="brand__rule"></span>
        <span class="brand__sub">Properties</span>
      </span>
    </div>
    <p class="website">www.halvernproperties-example.com</p>
  </section>
</body>
</html>
```